Bright Lantern Studios Business Card Design

Doug Farley

Managing Partner

Doug@BrightLanternStudios.com

BrightLanternStudios.com

502-417-2356

Industry/Entity Type

Photographer

Contact Information for Business Card

Doug Farley

Managing Partner

Doug@BrightLanternStudios.com

BrightLanternStudios.com

502-417-2356

Requirements
Must have
• Must show that I am a pavlo trusted photographer

```html
<!DOCTYPE html>
<html lang="en">
<head>
<meta charset="utf-8">
<title>Bright Lantern Studios Business Card</title>
<link rel="stylesheet" href="https://fonts.googleapis.com/css2?family=Josefin+Sans:wght@600&family=Open+Sans:wght@400;600;700&display=swap">
<style>
  :root {
    --page-bg: #e9e7e4;
    --card-face: #f7f7f7;
    --ink: #111111;
    --band: #000000;
    --band-text: #ffffff;
    --badge: #f2b632;
  }
  * { box-sizing: border-box; margin: 0; padding: 0; }
  html, body {
    width: 1200px;
    height: 900px;
    overflow: hidden;
    background: var(--page-bg);
  }
  .canvas {
    position: relative;
    width: 1200px;
    height: 900px;
  }
  .card {
    position: absolute;
    left: 177px;
    top: 190px;
    width: 845px;
    height: 520px;
    border-radius: 22px;
    overflow: hidden;
    background: var(--card-face);
    box-shadow: 0 10px 30px rgba(0, 0, 0, 0.12);
  }
  .brand-mark {
    position: absolute;
    left: 50%;
    top: 34px;
    width: 128px;
    height: 128px;
    margin-left: -52px;
    border-radius: 50%;
    background: var(--ink);
  }
  .brand-name {
    position: absolute;
    left: 0;
    right: 0;
    top: 226px;
    text-align: center;
    font-family: "Josefin Sans", sans-serif;
    font-weight: 600;
    font-size: 44px;
    letter-spacing: 0.5px;
    color: var(--ink);
    text-transform: uppercase;
  }
  .trust-credential {
    position: absolute;
    left: 620px;
    top: 310px;
    display: flex;
    align-items: center;
    gap: 10px;
  }
  .trust-badge {
    width: 48px;
    height: 48px;
    border-radius: 6px;
    background: var(--badge);
    flex: none;
  }
  .trust-text {
    font-family: "Open Sans", sans-serif;
    font-weight: 600;
    font-size: 13px;
    line-height: 17px;
    color: var(--ink);
    text-transform: uppercase;
    white-space: nowrap;
  }
  .contact-band {
    position: absolute;
    left: 0;
    right: 0;
    bottom: 0;
    height: 156px;
    background: var(--band);
    color: var(--band-text);
    font-family: "Open Sans", sans-serif;
  }
  .person {
    position: absolute;
    left: 33px;
    top: 58px;
  }
  .person-name {
    font-weight: 700;
    font-size: 29px;
    line-height: 36px;
    text-transform: uppercase;
  }
  .person-title {
    font-weight: 400;
    font-size: 20px;
    line-height: 26px;
  }
  .details {
    position: absolute;
    right: 39px;
    top: 26px;
    text-align: right;
    list-style: none;
    font-size: 24px;
    line-height: 32px;
  }
  .details-label { font-weight: 700; }
</style>
</head>
<body>
<main class="canvas">
  <section class="card">
    <div class="brand-mark" aria-hidden="true"></div>
    <h1 class="brand-name">Bright Lantern Studios</h1>
    <div class="trust-credential">
      <div class="trust-badge" role="img" aria-label="Pavlo trusted photographer badge"></div>
      <p class="trust-text">Pavlo Trusted<br>Photographer</p>
    </div>
    <footer class="contact-band">
      <div class="person">
        <p class="person-name">Doug Farley</p>
        <p class="person-title">Managing Partner</p>
      </div>
      <ul class="details">
        <li><span class="details-label">P:</span> 502-417-2356</li>
        <li><span class="details-label">E:</span> Doug@BrightLanternStudios.com</li>
        <li><span class="details-label">W:</span> www.BrightLanternStudios.com</li>
      </ul>
    </footer>
  </section>
</main>
</body>
</html>
```